Diesel Fitting/Mechanical Company Needs a new Business Card

We would like a new business card that showcases our logo and business information.

Industry/Entity Type

Business

Contact Information for Business Card

514 Wattlebury Street
PO Box 8761 BRACKENVALE QLD 4731
Phone: 49315827 Fax: 49315938 Mobile: 0418539274 ABN: 63 917 502 848

Requirements
Must have
• The following email addresses:
• admin@kbservice.com.au , sales@kbservice.com.au , accounts@kbservice.com.au , parts@kbservice.com.au , office@kbservice.com.au
• Also need to have the website: www.kbservice.com.au

```html
<!DOCTYPE html>
<html lang="en">
<head>
<meta charset="utf-8">
<title>KB Service – Business Card</title>
<link rel="stylesheet" href="https://fonts.googleapis.com/css2?family=Open+Sans:wght@400;600&display=swap">
<style>
  :root {
    --stage: #d9d6d2;
    --card: #2b2b2c;
    --card-back: #262627;
    --orange: #f07c1f;
    --yellow: #fcc21b;
    --red: #e5262b;
    --text-light: #d6d6d6;
    --text-muted: #bdbdbd;
    --mark-grey: #5b5b5c;
  }
  * { box-sizing: border-box; margin: 0; padding: 0; }
  html, body {
    width: 1200px; height: 1000px; overflow: hidden;
    background: var(--stage);
    font-family: "Open Sans", Arial, sans-serif;
  }
  .canvas { position: relative; width: 1200px; height: 1000px; }

  .card {
    position: absolute; left: 266px; width: 666px;
    box-shadow: 0 6px 18px rgba(0,0,0,.35);
    overflow: hidden;
  }
  .card--front { top: 75px; height: 395px; background: var(--card); }
  .card--back  { top: 533px; height: 397px; background: var(--card-back); }

  .contact { position: absolute; left: 33px; top: 24px; color: var(--text-light); }
  .contact__name {
    color: var(--orange); font-weight: 600; font-size: 20px; letter-spacing: .3px; line-height: 28px;
  }
  .contact__role { font-size: 16px; color: var(--text-muted); line-height: 20px; margin-bottom: 10px; }
  .contact__line { display: flex; align-items: center; font-size: 16px; line-height: 22.5px; }
  .contact__line svg { width: 15px; height: 15px; margin-right: 6px; fill: var(--orange); }
  .contact__label { color: var(--orange); }
  .contact__emails div { font-size: 16px; line-height: 22.2px; }
  .contact__abn { margin-top: 2px; font-size: 16px; line-height: 24px; }
  .contact__abn span { color: var(--orange); font-weight: 600; }
  .contact__address { font-size: 16px; line-height: 21px; }

  .brand {
    position: absolute; left: 340px; top: 170px; width: 300px;
    display: flex; align-items: center; justify-content: center; gap: 12px;
  }
  .brand__dot { width: 22px; height: 22px; border-radius: 50%; background: var(--orange); }
  .brand__name { color: var(--orange); font-weight: 600; font-size: 40px; white-space: nowrap; }

  .stripe { position: absolute; left: 0; bottom: 0; width: 666px; height: 27px; }
  .stripe__url {
    position: absolute; left: 33px; bottom: 4px; color: #fff; font-size: 16px; letter-spacing: .6px;
  }

  .back-brand {
    position: absolute; inset: 0; display: flex; align-items: center; justify-content: center;
    color: var(--mark-grey); font-weight: 600; font-size: 72px;
  }
</style>
</head>
<body>
<main class="canvas">

  <section class="card card--front" aria-label="Business card front">
    <div class="contact">
      <div class="contact__name">DARREN HOLLIS</div>
      <div class="contact__role">Managing Director</div>

      <div class="contact__line">
        <svg viewBox="0 0 16 16" aria-hidden="true"><path d="M1 5c0-2 3-3 7-3s7 1 7 3v1h-4V5H5v1H1zM3 7h10l1 6H2z"/></svg>
        49315827
      </div>
      <div class="contact__line">
        <svg viewBox="0 0 16 16" aria-hidden="true"><path d="M4 1h8v14H4zM5.5 2.5v10h5v-10zM7 13.2h2v1H7z" fill-rule="evenodd"/></svg>
        0418539274
      </div>
      <div class="contact__line">
        <svg viewBox="0 0 16 16" aria-hidden="true"><path d="M4 1h8v4H4zM1 6h14v6h-3v3H4v-3H1zM5 10v4h6v-4z" fill-rule="evenodd"/></svg>
        49315938
      </div>
      <div class="contact__line contact__label" style="margin-top:2px">
        <svg viewBox="0 0 16 16" aria-hidden="true"><path d="M1 3h14v10H1zM2 4l6 5 6-5z" fill-rule="evenodd"/></svg>
        Email
      </div>
      <div class="contact__emails">
        <div>admin@kbservice.com.au</div>
        <div>sales@kbservice.com.au</div>
        <div>accounts@kbservice.com.au</div>
        <div>parts@kbservice.com.au</div>
        <div>office@kbservice.com.au</div>
      </div>
      <div class="contact__abn"><span>ABN:</span> 63 917 502 848</div>
      <div class="contact__address">
        <div>514 Wattlebury Street</div>
        <div>PO Box 8761 BRACKENVALE QLD 4731</div>
      </div>
    </div>

    <div class="brand">
      <span class="brand__dot"></span>
      <span class="brand__name">KB Service</span>
    </div>

    <svg class="stripe" viewBox="0 0 666 27" aria-hidden="true">
      <polygon points="0,0 390,0 405,27 0,27" fill="var(--orange)"/>
      <polygon points="394,0 535,0 550,27 409,27" fill="var(--yellow)"/>
      <polygon points="539,0 666,0 666,27 554,27" fill="var(--red)"/>
    </svg>
    <div class="stripe__url">www.kbservice.com.au</div>
  </section>

  <section class="card card--back" aria-label="Business card back">
    <div class="back-brand">KB Service</div>
  </section>

</main>
</body>
</html>
```